Brindle Grass Services website design

We want to create a Sports turf website for our business Brindle Grass Services - we do sports turf management on sports fields around the Mackay region soccer rugby league softball fields etc from full turf management plans and maintenance to just supply and apply of turf management products and just supply of products with program we also do grounds facility maintenance at council facility's and grounds that require a higher level of care - we will up load our logos and fonts etc to assist with the colour pallet for the website - we will have to have a landing page a shop page with tabs a gallery tab along with a grants initiative and our coastals finest green tab also - our font for the txt is called ethnocentric
Updates

how do we open time for people to submit we have no one submitted

Industry/Entity Type

Turf

Coding

Coded - Design and coding required

Number of Pages Required

5+ page

Font styles to use
Other font styles liked:
• ethnocentric

Requirements
Must have
• I have mentioned some waffle in the description that should assist
Should not have
• anything not related

```html
<!DOCTYPE html>
<html lang="en">
<head>
<meta charset="utf-8">
<title>Brindle Grass Services</title>
<link href="https://fonts.googleapis.com/css2?family=Audiowide&family=Poppins:wght@400;500;600;700&display=swap" rel="stylesheet">
<style>
:root{
  --green-dark:#0b6e2b;
  --green:#1e9a3c;
  --green-bright:#35b84a;
  --lime:#7cc242;
  --blue:#17a2e6;
  --blue-pale:#e5f4fc;
  --ink:#1c1c1c;
  --grey:#6a6a6a;
  --footer:#0e0f0e;
  --white:#fff;
}
*{box-sizing:border-box;margin:0;padding:0}
html,body{width:1200px;height:4902px;overflow:hidden}
body{font-family:"Poppins",sans-serif;color:var(--ink);background:var(--white);position:relative}
.abs{position:absolute}
.display{font-family:"Audiowide",sans-serif;text-transform:uppercase;letter-spacing:1px}
.btn{position:absolute;display:flex;align-items:center;justify-content:space-between;padding:0 18px;background:var(--blue);color:#fff;font-size:11px;font-weight:600;text-transform:uppercase;letter-spacing:.3px}
.btn svg{width:10px;height:14px}
.btn.green{background:var(--green)}
.ph{position:absolute}

/* nav */
.topline{top:0;left:0;width:1200px;height:4px;background:var(--green)}
.nav{top:4px;left:0;width:1200px;height:66px}
.logo{position:absolute;font-weight:700;font-size:17px;color:var(--ink);display:flex;align-items:center;gap:8px}
.logo i{display:block;width:12px;height:12px;background:var(--green-bright);border-radius:50%}
.nav-links{position:absolute;left:505px;top:26px;display:flex;gap:28px;font-size:10.5px;font-weight:500;text-transform:uppercase}

/* hero */
.hero{top:70px;left:0;width:1200px;height:596px;overflow:hidden}
.hero h1{position:absolute;left:122px;top:108px;font-size:57px;line-height:62px;color:#fff;font-weight:400}
.hero p{position:absolute;left:122px;top:292px;width:600px;font-size:12px;line-height:17px;color:#fff}

/* about */
.about-title{left:640px;top:735px;font-size:31px;line-height:37px}
.about-text{left:640px;top:822px;width:430px;font-size:11px;line-height:17.5px;color:var(--grey)}
.ticks{left:640px;top:910px;list-style:none;font-size:11px}
.ticks li{display:flex;align-items:center;gap:14px;height:36px}
.ticks li::before{content:"";width:0;height:0;border-left:6px solid transparent;border-right:6px solid transparent;border-bottom:10px solid var(--green)}

/* services */
.services{top:1246px;left:0;width:1200px;height:571px;background:var(--blue-pale)}
.section-title{position:absolute;left:0;width:1200px;text-align:center;font-size:30px}
.card{position:absolute;width:224px;height:325px;background:#fff;border-radius:10px;top:1359px;text-align:center}
.card.active{background:var(--green);color:#fff}
.card .icon{position:absolute;left:77px;top:32px;width:70px;height:70px;border-radius:50%;background:#e2f3e5;display:flex;align-items:center;justify-content:center}
.card .icon span{width:46px;height:46px;border-radius:50%;background:var(--green);border:3px solid #fff;display:flex;align-items:center;justify-content:center}
.card h3{position:absolute;left:0;width:100%;top:124px;font-size:15px;line-height:19px;font-weight:500}
.card .ph{left:12px;top:180px;width:200px;height:134px;border:3px solid #111;border-radius:4px}

/* why */
.why-title{left:122px;top:1905px;font-size:31px;line-height:37px}
.feature{position:absolute;width:280px}
.feature .ficon{position:absolute;left:0;top:4px;width:76px;height:76px;border-radius:50%;background:#e7f5ea;display:flex;align-items:center;justify-content:center}
.feature .ficon span{width:48px;height:48px;border-radius:50%;background:#fff;border:2px solid var(--green);display:flex;align-items:center;justify-content:center}
.feature h4{position:absolute;left:90px;top:0;font-size:15px;font-weight:500}
.feature p{position:absolute;left:90px;top:24px;width:180px;font-size:10.5px;line-height:17px;color:var(--grey)}

/* how */
.how-band{top:2402px;left:122px;width:956px;height:215px;border-radius:40px;overflow:hidden;display:flex}
.how-step{flex:1;text-align:center;color:#fff;position:relative}
.how-step .sicon{margin:38px auto 0;width:60px;height:60px;border-radius:50%;background:#fff;display:flex;align-items:center;justify-content:center;border:4px solid rgba(255,255,255,.4);background-clip:padding-box}
.how-step h4{margin-top:22px;font-size:15px;font-weight:500}
.how-step p{margin:8px auto 0;width:250px;font-size:10.5px;line-height:16px}

/* gallery */
.slide{position:absolute;top:2733px;height:308px;border-radius:4px}
.tag{position:absolute;top:2750px;color:#fff;font-size:19px;letter-spacing:1px}
.arrow{position:absolute;top:2880px;width:24px;height:24px;border:1.5px solid var(--ink);border-radius:50%;display:flex;align-items:center;justify-content:center}

/* products */
.products{top:3159px;left:0;width:1200px;height:733px;background:var(--lime)}
.pcard{position:absolute;background:#fff;border-radius:10px}
.pcard h3{position:absolute;font-size:16px;font-weight:600;line-height:20px}
.pcard p{position:absolute;font-size:10px;line-height:14px;color:var(--grey)}
.price{position:absolute;width:74px;height:74px;border-radius:50%;background:var(--green);border:4px solid #fff;color:#fff;font-weight:600;font-size:16px;display:flex;align-items:center;justify-content:center;box-shadow:0 0 0 2px var(--green)}

/* contact */
.form-card{top:3958px;left:122px;width:479px;height:371px;background:var(--blue-pale)}
.form-head{position:absolute;left:6px;top:4px;width:467px;height:46px;background:#1c1c1c;color:#fff;font-size:27px;display:flex;align-items:center;justify-content:center}
.field{position:absolute;background:#fff;border:1px solid #c9d6de;font-size:10.5px;padding:10px 10px;color:var(--ink)}

/* cta */
.cta{top:4386px;left:122px;width:956px;height:248px;background:var(--green);border-radius:40px;overflow:hidden}
.cta h2{position:absolute;left:430px;top:48px;font-size:31px;line-height:38px;color:#fff;font-weight:400}
.cta p{position:absolute;left:430px;top:128px;font-size:11px;line-height:17px;color:#fff}

/* footer */
.footer{top:4643px;left:0;width:1200px;height:259px;background:var(--footer);color:#fff}
.footer h5{position:absolute;top:40px;font-family:"Audiowide",sans-serif;font-size:11.5px;letter-spacing:1.5px;font-weight:400}
.footer ul{position:absolute;list-style:none;font-size:9px;line-height:18px}
.footer .copy{position:absolute;left:0;width:1200px;bottom:8px;text-align:center;font-size:8px;color:#bbb}
</style>
</head>
<body>

<div class="abs topline"></div>
<header class="abs nav">
  <div class="logo" style="left:122px;top:22px"><i></i>BRINDLE GRASS</div>
  <nav class="nav-links"><span>Services</span><span>About Us</span><span>Shop</span><span>Gallery</span><span>Grants &amp; Initiatives</span></nav>
  <div class="btn" style="left:950px;top:20px;width:127px;height:34px;font-size:10.5px">Contact Us <svg viewBox="0 0 10 14"><path d="M5 0C3 4 1 6 1 9a4 4 0 0 0 8 0c0-3-2-5-4-9z" fill="#fff"/></svg></div>
</header>

<section class="abs hero">
  <div class="ph" role="img" aria-label="Ride-on mower cutting a lush sports field" style="inset:0;background:linear-gradient(180deg,#1d2b2a 0%,#2e4a36 40%,#3f7a31 70%,#5b9a38 100%)"></div>
  <h1 class="display">Performance<br>starts from<br>the ground up</h1>
  <p>From local sports clubs to major council facilities, Brindle Grass Services delivers professional turf care and facility maintenance with precision, reliability, and results that stand out on game day.</p>
  <div class="btn" style="left:122px;top:356px;width:255px;height:40px">Get your free estimate today <svg viewBox="0 0 10 14"><path d="M5 0C3 4 1 6 1 9a4 4 0 0 0 8 0c0-3-2-5-4-9z" fill="#fff"/></svg></div>
  <svg class="abs" style="left:0;top:0" width="1200" height="596" viewBox="0 0 1200 596">
    <path d="M0 430 Q600 780 1200 430" fill="none" stroke="#1e9a3c" stroke-width="6"/>
    <path d="M0 440 Q600 790 1200 440 L1200 596 L0 596Z" fill="#fff"/>
  </svg>
</section>

<!-- about -->
<div class="ph" role="img" aria-label="Line of maintenance mowers on a field" style="left:122px;top:729px;width:356px;height:156px;border:3px solid #d8eedd;border-radius:4px;background:linear-gradient(180deg,#3a4e3c,#5f9a48)"></div>
<div class="ph" role="img" aria-label="Aerial view of a stadium playing surface" style="left:122px;top:890px;width:356px;height:223px;border:3px solid #d8eedd;border-radius:0 0 60px 60px;background:linear-gradient(180deg,#8fb4d8 0%,#6e9a6a 35%,#2f8a3d 100%)"></div>
<div class="abs" style="left:416px;top:854px;width:100px;height:100px;border-radius:50%;background:var(--blue);border:5px solid #fff;display:flex;align-items:center;justify-content:center"><svg width="34" height="48" viewBox="0 0 10 14"><path d="M5 0C3 4 1 6 1 9a4 4 0 0 0 8 0c0-3-2-5-4-9z" fill="none" stroke="#fff" stroke-width="1.2"/></svg></div>
<div class="abs" style="left:600px;top:723px;width:2px;height:385px;background:#dcdcdc"></div>
<svg class="abs" style="left:1100px;top:800px" width="100" height="190" viewBox="0 0 10 14"><path d="M5 0C3 4 1 6 1 9a4 4 0 0 0 8 0c0-3-2-5-4-9z" fill="#eaf6fd"/></svg>
<h2 class="abs display about-title">About Brindle<br>Grass Services</h2>
<p class="abs about-text">At Brindle Grass Services, we're passionate about growing and maintaining world-class sports turf across the Mackay region. With years of local experience, we provide end-to-end solutions — from turf maintenance programs to product supply and facility care for councils, schools, and sporting clubs.</p>
<ul class="abs ticks">
  <li>Local experts serving Mackay's sports fields and community clubs</li>
  <li>Complete turf management &amp; maintenance programs</li>
  <li>High-quality turf products and application services</li>
  <li>Grounds &amp; facility maintenance for councils and premium venues</li>
</ul>
<div class="btn" style="left:640px;top:1064px;width:190px;height:37px">Learn more about us <svg viewBox="0 0 10 14"><path d="M5 0C3 4 1 6 1 9a4 4 0 0 0 8 0c0-3-2-5-4-9z" fill="#fff"/></svg></div>

<!-- services -->
<section class="abs services"></section>
<svg class="abs" style="left:0;top:1140px" width="1200" height="110" viewBox="0 0 1200 110">
  <text x="0" y="102" textLength="1200" lengthAdjust="spacingAndGlyphs" font-family="Audiowide, sans-serif" font-size="112" fill="none" stroke="#e6e6e6" stroke-width="1.5">BRINDLE GRASS SERVICES</text>
</svg>
<h2 class="section-title display" style="top:1295px">Our Services</h2>
<div class="card" style="left:122px"><div class="icon"><span><svg width="20" height="20" viewBox="0 0 20 20"><circle cx="10" cy="10" r="7" fill="none" stroke="#fff" stroke-width="2"/></svg></span></div><h3>Sports Turf<br>Management</h3><div class="ph" role="img" aria-label="Junior players training on a sports field"style="background:linear-gradient(180deg,#9fbfa0,#4d8e3a)"></div></div>
<div class="card" style="left:365px"><div class="icon"><span><svg width="20" height="20" viewBox="0 0 20 20"><rect x="4" y="4" width="12" height="12" fill="none" stroke="#fff" stroke-width="2"/></svg></span></div><h3>Product Supply<br>&amp; Application</h3><div class="ph" role="img" aria-label="Worker checking a product delivery" style="background:linear-gradient(180deg,#7a5a3a,#2f5fa5)"></div></div>
<div class="card active" style="left:611px"><div class="icon" style="background:rgba(255,255,255,.25)"><span><svg width="20" height="20" viewBox="0 0 20 20"><rect x="3" y="5" width="14" height="10" rx="2" fill="none" stroke="#fff" stroke-width="2"/></svg></span></div><h3>Grounds &amp;<br>Facility Maintenance</h3><div class="ph" role="img" aria-label="Freshly mown grounds beside a fence" style="background:linear-gradient(180deg,#b8c6cc,#5f8e44)"></div></div>
<div class="card" style="left:854px"><div class="icon"><span><svg width="20" height="20" viewBox="0 0 20 20"><rect x="3" y="5" width="14" height="10" rx="2" fill="none" stroke="#fff" stroke-width="2"/></svg></span></div><h3>Custom Turf<br>Programs</h3><div class="ph" role="img" aria-label="Consultant planning a turf program on a laptop" style="background:linear-gradient(180deg,#3b3f46,#6fa14a)"></div></div>
<div class="btn" style="left:497px;top:1716px;width:171px;height:39px">View all services <svg viewBox="0 0 10 14"><path d="M5 0C3 4 1 6 1 9a4 4 0 0 0 8 0c0-3-2-5-4-9z" fill="#fff"/></svg></div>

<!-- why -->
<h2 class="abs display why-title">Why choose Brindle<br>Grass Services</h2>
<div class="feature" style="left:122px;top:2001px"><div class="ficon"><span><svg width="20" height="20" viewBox="0 0 20 20"><rect x="5" y="3" width="10" height="14" rx="1" fill="none" stroke="#0b6e2b" stroke-width="2"/></svg></span></div><h4>Local Expertise</h4><p>We live and work in the Mackay region — so we understand the local conditions and what it takes to keep fields thriving year-round.</p></div>
<div class="feature" style="left:460px;top:2001px"><div class="ficon"><span><svg width="20" height="20" viewBox="0 0 20 20"><circle cx="10" cy="10" r="6" fill="none" stroke="#0b6e2b" stroke-width="2"/></svg></span></div><h4>Professional Standards</h4><p>Our turf care programs are trusted by councils, schools, and sporting clubs for their consistency, reliability, and results.</p></div>
<div class="feature" style="left:122px;top:2134px"><div class="ficon"><span><svg width="20" height="20" viewBox="0 0 20 20"><path d="M10 2l7 3v5c0 4-3 7-7 8-4-1-7-4-7-8V5z" fill="none" stroke="#0b6e2b" stroke-width="2"/></svg></span></div><h4>Quality Products &amp; Equipment</h4><p>We use premium turf management products and professional-grade equipment to ensure healthy, durable playing surfaces.</p></div>
<div class="feature" style="left:460px;top:2134px"><div class="ficon"><span><svg width="20" height="20" viewBox="0 0 20 20"><circle cx="10" cy="11" r="6" fill="none" stroke="#0b6e2b" stroke-width="2"/><path d="M10 11V8" stroke="#0b6e2b" stroke-width="2"/></svg></span></div><h4>Tailored Solutions</h4><p>Every field is unique. We design turf programs that match your budget, schedule, and performance goals.</p></div>
<div class="ph" role="img" aria-label="Red turf aerator on a lawn" style="left:790px;top:1888px;width:287px;height:380px;border:3px solid #5a5a5a;border-radius:6px;background:linear-gradient(180deg,#8c8f90 0%,#b63c3c 50%,#5c8c3c 100%)"></div>

<!-- how -->
<div class="ph" role="img" aria-label="Soft grass blades fading into white" style="left:0;top:2270px;width:1200px;height:140px;background:linear-gradient(180deg,#fff,#eef5ef 70%,#fff)"></div>
<svg class="abs" style="left:0;top:2440px" width="1200" height="120" viewBox="0 0 1200 120"><path d="M0 20 Q80 30 140 80" fill="none" stroke="#0b6e2b" stroke-width="10"/><path d="M1200 20 Q1120 30 1060 80" fill="none" stroke="#0b6e2b" stroke-width="10"/></svg>
<h2 class="section-title display" style="top:2342px">How it works</h2>
<div class="abs how-band">
  <div class="how-step" style="background:var(--green-dark)"><div class="sicon"><svg width="22" height="22" viewBox="0 0 20 20"><rect x="4" y="4" width="12" height="13" rx="2" fill="none" stroke="#0b6e2b" stroke-width="2"/></svg></div><h4>Site Assessment</h4><p>We inspect your field's condition, soil health, &amp; current turf performance.</p></div>
  <div class="how-step" style="background:var(--green)"><div class="sicon"><svg width="22" height="22" viewBox="0 0 20 20"><rect x="3" y="5" width="14" height="10" rx="2" fill="none" stroke="#1e9a3c" stroke-width="2"/></svg></div><h4>Tailored Program</h4><p>We design a customized management plan to enhance turf quality &amp; playability.</p></div>
  <div class="how-step" style="background:var(--green-bright)"><div class="sicon"><svg width="22" height="22" viewBox="0 0 20 20"><path d="M4 14l5-5 3 3 4-6" fill="none" stroke="#35b84a" stroke-width="2.5"/></svg></div><h4>Implementation &amp; Support</h4><p>From supply to application, we provide ongoing care &amp; monitoring for lasting results.</p></div>
</div>
<svg class="abs" style="left:320px;top:2460px" width="560" height="40" viewBox="0 0 560 40"><path d="M0 10 Q140 40 280 10 Q420 40 560 10" fill="none" stroke="#fff" stroke-dasharray="3 4" opacity=".6"/></svg>

<!-- gallery -->
<h2 class="section-title display" style="top:2673px">Our Project Gallery</h2>
<div class="slide" role="img" aria-label="Previous project: roof restoration" style="left:122px;width:131px;background:linear-gradient(180deg,#4a4d50,#8a8d90)"></div>
<div class="slide" role="img" aria-label="Bare turf patch before treatment" style="left:266px;width:334px;border-radius:4px 0 0 4px;background:linear-gradient(160deg,#6a7048,#8a7a42 50%,#5c5a36)"></div>
<div class="slide" role="img" aria-label="Same area after turf established" style="left:600px;width:334px;border-radius:0 4px 4px 0;background:linear-gradient(180deg,#8e9aa0 0%,#3f8a36 35%,#5ea33f 100%)"></div>
<div class="slide" role="img" aria-label="Next project: roof restoration" style="left:947px;width:130px;background:linear-gradient(180deg,#4a4d50,#8a8d90)"></div>
<div class="tag" style="left:284px">BEFORE</div>
<div class="tag" style="left:855px">AFTER</div>
<div class="abs" style="left:599px;top:2733px;width:2px;height:308px;background:#fff"></div>
<div class="abs" style="left:574px;top:2862px;width:52px;height:52px;border-radius:50%;background:#fff;display:flex;align-items:center;justify-content:center"><svg width="24" height="14" viewBox="0 0 24 14"><path d="M10 1L3 7l7 6zM14 1l7 6-7 6z" fill="#1c1c1c"/></svg></div>
<div class="arrow" style="left:87px"><svg width="8" height="10" viewBox="0 0 8 10"><path d="M6 1L2 5l4 4" fill="none" stroke="#1c1c1c" stroke-width="1.5"/></svg></div>
<div class="arrow" style="left:1086px"><svg width="8" height="10" viewBox="0 0 8 10"><path d="M2 1l4 4-4 4" fill="none" stroke="#1c1c1c" stroke-width="1.5"/></svg></div>

<!-- products -->
<svg class="abs" style="left:0;top:3060px" width="1200" height="100" viewBox="0 0 1200 100"><text x="0" y="96" textLength="1200" lengthAdjust="spacingAndGlyphs" font-family="Audiowide, sans-serif" font-size="104" fill="none" stroke="#ececec" stroke-width="1.5">BRINDLE GRASS SERVICES</text></svg>
<section class="abs products"></section>
<svg class="abs" style="left:540px;top:3126px" width="120" height="34" viewBox="0 0 120 34"><path d="M0 34 L60 0 L120 34Z" fill="#7cc242"/></svg>
<h2 class="section-title display" style="top:3208px;color:#fff">Featured Turf Products</h2>

<div class="pcard" style="left:122px;top:3273px;width:468px;height:238px">
  <h3 style="left:25px;top:52px">HydraSoak Liquid<br>Wetting Agent.</h3>
  <p style="left:25px;top:100px;width:210px">Boost turf color, density, and resilience with our slow-release professional fertilizer designed for sports-grade performance.</p>
  <div class="btn green" style="left:25px;top:162px;width:116px;height:37px;font-size:10px">Shop now <svg viewBox="0 0 10 14"><path d="M5 0C3 4 1 6 1 9a4 4 0 0 0 8 0c0-3-2-5-4-9z" fill="#fff"/></svg></div>
  <div class="ph" role="img" aria-label="Two containers of liquid wetting agent on grass" style="left:262px;top:0;width:192px;height:226px;border-radius:0 0 10px 40px;border:3px solid #e3ecd9;background:linear-gradient(180deg,#eef0f0,#cfd6d2 55%,#6ea345)"></div>
  <div class="price" style="left:230px;top:140px">$25.19</div>
</div>
<div class="pcard" style="left:122px;top:3534px;width:468px;height:234px">
  <div class="ph" role="img" aria-label="Granular turf product bag and bottle" style="left:14px;top:0;width:196px;height:220px;border-radius:0 0 10px 40px;border:3px solid #e3ecd9;background:linear-gradient(180deg,#e8ebe8,#c6d0c5 55%,#6ea345)"></div>
  <h3 style="left:240px;top:78px">TerraGuard GR</h3>
  <p style="left:240px;top:100px;width:210px">Ensure even water penetration and prevent dry spots across your field for a consistent, lush playing surface.</p>
  <div class="btn green" style="left:240px;top:154px;width:116px;height:37px;font-size:10px">Shop now <svg viewBox="0 0 10 14"><path d="M5 0C3 4 1 6 1 9a4 4 0 0 0 8 0c0-3-2-5-4-9z" fill="#fff"/></svg></div>
  <div class="price" style="left:388px;top:10px">$25.19</div>
</div>
<div class="pcard" style="left:615px;top:3273px;width:463px;height:495px">
  <div class="ph" role="img" aria-label="Pail and bottle of soil conditioner on grass" style="left:4px;top:4px;width:455px;height:398px;border-radius:6px;background:linear-gradient(180deg,#3c3c3c 0%,#c9a94a 35%,#e8cf3a 60%,#5f9a3d 100%)"></div>
  <div class="price" style="left:358px;top:20px">$25.19</div>
  <h3 style="left:16px;top:415px">RootPrime</h3>
  <p style="left:16px;top:436px;width:220px">Improve soil structure and nutrient uptake with this powerful blend that enhances turf health from the ground up.</p>
  <div class="btn green" style="left:327px;top:430px;width:116px;height:37px;font-size:10px">Shop now <svg viewBox="0 0 10 14"><path d="M5 0C3 4 1 6 1 9a4 4 0 0 0 8 0c0-3-2-5-4-9z" fill="#fff"/></svg></div>
</div>
<div class="btn" style="left:512px;top:3806px;width:176px;height:36px;background:transparent;border:1.5px solid #fff;font-size:10px">View all products <svg viewBox="0 0 10 14"><path d="M5 0C3 4 1 6 1 9a4 4 0 0 0 8 0c0-3-2-5-4-9z" fill="#fff"/></svg></div>

<!-- contact -->
<div class="abs form-card">
  <div class="form-head display">Get in touch</div>
  <div class="field" style="left:10px;top:64px;width:226px;height:34px">First Name*</div>
  <div class="field" style="left:244px;top:64px;width:226px;height:34px">Last Name*</div>
  <div class="field" style="left:10px;top:108px;width:226px;height:34px">Email*</div>
  <div class="field" style="left:244px;top:108px;width:226px;height:34px">Phone*</div>
  <div class="field" style="left:10px;top:152px;width:460px;height:98px">Message*</div>
  <div class="btn" style="left:173px;top:268px;width:134px;height:38px">Submit <svg viewBox="0 0 10 14"><path d="M5 0C3 4 1 6 1 9a4 4 0 0 0 8 0c0-3-2-5-4-9z" fill="#fff"/></svg></div>
</div>
<div class="ph" role="img" aria-label="Stocked turf product shelves and a mower" style="left:723px;top:3966px;width:354px;height:146px;border:3px solid #d8eedd;border-radius:4px;background:linear-gradient(180deg,#9a9488,#5c6a4a)"></div>
<div class="ph" role="img" aria-label="Striped lawn with a red mower" style="left:723px;top:4116px;width:354px;height:210px;border:3px solid #d8eedd;border-radius:0 0 60px 60px;background:linear-gradient(180deg,#9fb6c8 0%,#4f9a3c 30%,#2f7a2f 100%)"></div>

<!-- cta -->
<svg class="abs" style="left:0;top:4420px" width="1200" height="200" viewBox="0 0 1200 200"><path d="M0 120 Q60 130 124 190" fill="none" stroke="#0b6e2b" stroke-width="10"/><path d="M1200 60 Q1130 70 1076 140" fill="none" stroke="#0b6e2b" stroke-width="10"/></svg>
<svg class="abs" style="left:580px;top:4356px" width="60" height="32" viewBox="0 0 60 32"><path d="M0 32 L30 0 L60 32Z" fill="#1e9a3c"/></svg>
<section class="abs cta">
  <div class="ph" role="img" aria-label="Mown turf stripes" style="left:38px;top:40px;width:250px;height:208px;border-radius:0 0 60px 60px;background:linear-gradient(90deg,#0b6e2b,#35b84a)"></div>
  <h2 class="display">Let's keep your<br>turf in top shape</h2>
  <p>Ready to improve your field's performance and presentation?<br>Contact our team for a free consultation or site visit.</p>
  <div class="btn" style="left:430px;top:180px;width:152px;height:38px">Call us today <svg viewBox="0 0 10 14"><path d="M5 0C3 4 1 6 1 9a4 4 0 0 0 8 0c0-3-2-5-4-9z" fill="#fff"/></svg></div>
  <div class="abs" style="left:600px;top:183px;display:flex;align-items:center;gap:10px;color:#fff;font-size:21px;font-weight:500">
    <span style="width:30px;height:30px;border-radius:50%;background:var(--lime);display:flex;align-items:center;justify-content:center"><svg width="16" height="16" viewBox="0 0 24 24"><path d="M6.6 10.8a15 15 0 0 0 6.6 6.6l2.2-2.2c.3-.3.7-.4 1-.2 1.1.4 2.3.6 3.6.6.6 0 1 .4 1 1V20c0 .6-.4 1-1 1A17 17 0 0 1 3 4c0-.6.4-1 1-1h3.5c.6 0 1 .4 1 1 0 1.3.2 2.5.6 3.6.1.3 0 .7-.2 1z" fill="#fff"/></svg></span>(555) 014-2290</div>
</section>

<!-- footer -->
<footer class="abs footer">
  <div class="logo" style="left:122px;top:36px;color:#fff"><i></i>BRINDLE GRASS</div>
  <p class="abs" style="left:122px;top:74px;width:200px;font-size:9px;line-height:14px">Based in the Mackay region, Brindle Grass Services specializes in turf solutions for sports facilities, councils, and private grounds.</p>
  <div class="abs" style="left:122px;top:152px;display:flex;gap:6px"><span style="width:22px;height:22px;border:1px solid #fff;border-radius:50%"></span><span style="width:22px;height:22px;border:1px solid #fff;border-radius:50%"></span><span style="width:22px;height:22px;border:1px solid #fff;border-radius:50%"></span></div>
  <h5 style="left:352px">Quick Links</h5>
  <ul style="left:352px;top:66px"><li>Home</li><li>Services</li><li>About Us</li><li>Shop</li><li>Gallery</li><li>Grants &amp; Initiatives</li><li>Contact Us</li></ul>
  <h5 style="left:508px">Contact Us</h5>
  <ul style="left:508px;top:64px;line-height:36px"><li style="display:flex;align-items:center;gap:8px"><span style="width:18px;height:18px;border:1px solid #fff;border-radius:50%"></span>(555) 014-2290</li><li style="display:flex;align-items:center;gap:8px;color:#35b84a"><span style="width:18px;height:18px;border:1px solid #fff;border-radius:50%"></span>hello@brindlegrass.example</li></ul>
  <h5 style="left:729px">Services</h5>
  <ul style="left:729px;top:64px;line-height:26px"><li>Sports Turf Management</li><li>Product Supply &amp; Application</li><li>Grounds &amp; Facility Maintenance</li><li>Custom Turf Programs</li></ul>
  <h5 style="left:927px">Follow Us On</h5>
  <div class="field" style="left:927px;top:68px;width:151px;height:36px;background:#0e0f0e;border-color:#444;color:#fff;font-size:9px">Enter Your Email</div>
  <div class="btn" style="left:927px;top:116px;width:126px;height:36px;font-size:10px">Submit <svg viewBox="0 0 10 14"><path d="M5 0C3 4 1 6 1 9a4 4 0 0 0 8 0c0-3-2-5-4-9z" fill="#fff"/></svg></div>
  <div class="abs" style="left:122px;top:228px;width:956px;height:1px;background:#333"></div>
  <div class="copy">©2025 Brindle Grass Services all Rights Reserved</div>
</footer>

</body>
</html>
```